New business card design needed for Trucking/Staffing company!

I am looking for a business card design. The business name is Keystone Haul Partners, LLC. This company is a staffing company for commercial drivers/truck drivers. Most of our customers are trucking/supply companies. Our colors are blue/black/white/grey. The info I have on my current business cards is
-Spot for a name
-2 lines for an address
-3 lines for Office, cell, and fax
-email
-website(currently on backside of card with logo but can go anywhere)
Updates

Project Deadline Extended
Reason: Open to more designs

Target Market(s)

Trucking companies, building supply companies

Industry/Entity Type

Business

Contact Information for Business Card

Edgy but professional

Font styles to use
Other font styles liked:
• Open to suggestions

Colors
0555a3
000000
ffffff
9d9d9d

Requirements
Must have
• Must have the logo incorporated

```html
<!DOCTYPE html>
<html lang="en">
<head>
<meta charset="utf-8">
<title>Keystone Haul Partners, LLC — Business Card</title>
<link rel="stylesheet" href="https://fonts.googleapis.com/css2?family=Arimo:wght@400;700&display=swap">
<style>
  :root {
    --brand-blue: #0555a3;
    --ink: #000000;
    --card-black: #1d1d1f;
    --paper: #ffffff;
    --grey: #9d9d9d;
    --text-grey: #6b6b6b;
    --backdrop: #e9e9e9;
  }
  * { box-sizing: border-box; margin: 0; padding: 0; }
  html, body {
    width: 1200px; height: 950px; overflow: hidden;
    background: var(--backdrop);
    font-family: "Arimo", Arial, sans-serif;
  }
  .canvas { position: relative; width: 1200px; height: 950px; }
  .card {
    position: absolute; left: 210px; width: 780px; height: 446px;
    box-shadow: 0 6px 18px rgba(0,0,0,.18);
    overflow: hidden;
  }
  .card--front { top: 19px; background: var(--card-black); }
  .card--back  { top: 485px; background: var(--paper); }

  .brand-name {
    position: absolute; display: flex; align-items: center; gap: 14px;
    font-weight: 700; text-transform: uppercase; letter-spacing: 1px;
    white-space: nowrap;
  }
  .brand-name__mark { width: 22px; height: 22px; flex: none; background: var(--brand-blue); }
  .card--front .brand-name {
    left: 50%; top: 50%; transform: translate(-50%, -50%);
    font-size: 38px; color: var(--paper);
  }
  .card--back .brand-name {
    left: 110px; top: 66px; font-size: 30px; color: var(--brand-blue);
  }

  .accent-bar { position: absolute; width: 16px; background: var(--brand-blue); }
  .accent-bar--contact { right: 0; top: 146px; height: 128px; }
  .accent-bar--person  { left: 0; top: 315px; height: 112px; }

  .contact-list {
    position: absolute; right: 34px; top: 152px;
    list-style: none; text-align: right;
    font-size: 17px; line-height: 29px; color: var(--text-grey);
  }
  .contact-list li { display: flex; justify-content: flex-end; align-items: center; gap: 10px; }
  .contact-list svg { width: 16px; height: 16px; fill: var(--brand-blue); }

  .person {
    position: absolute; left: 36px; top: 312px;
    color: var(--text-grey); font-size: 17px; line-height: 23px;
  }
  .person__name { color: var(--brand-blue); font-weight: 700; font-size: 22px; line-height: 30px; }
</style>
</head>
<body>
<main class="canvas">
  <section class="card card--front" aria-label="Card front">
    <div class="brand-name"><span class="brand-name__mark"></span>Keystone Haul Partners</div>
  </section>

  <section class="card card--back" aria-label="Card back">
    <div class="brand-name"><span class="brand-name__mark"></span>Keystone Haul Partners</div>

    <div class="accent-bar accent-bar--contact"></div>
    <ul class="contact-list">
      <li>555 0142 7781
        <svg viewBox="0 0 16 16" aria-hidden="true"><path d="M2 6c0-2 2-3 6-3s6 1 6 3v1h-3V5.5H5V7H2zM4 8h8l1 5H3z"/></svg>
      </li>
      <li>555 0167 3390
        <svg viewBox="0 0 16 16" aria-hidden="true"><path d="M4 1h8v14H4zM5.5 3v9h5V3zM7 13h2v1H7z" fill-rule="evenodd"/></svg>
      </li>
      <li>555 0189 2264
        <svg viewBox="0 0 16 16" aria-hidden="true"><path d="M4 1h7v4H4zM2 6h12v6H2zM4 10h8v5H4z"/></svg>
      </li>
      <li>mark@keystonehaul.com
        <svg viewBox="0 0 16 16" aria-hidden="true"><path d="M1 3h14v10H1zM2 4l6 5 6-5v-.2H2z"/></svg>
      </li>
    </ul>

    <div class="accent-bar accent-bar--person"></div>
    <div class="person">
      <p class="person__name">Mark Ellison</p>
      <p class="person__title">President</p>
      <p class="person__address">2716 Harrow Lane</p>
      <p class="person__address">Lakeview, PA 17402</p>
    </div>
  </section>
</main>
</body>
</html>
```